Menu Design for Indian Restaurant

We are a new Indian restaurant, named Spices of Sarani Restaurant, looking for a sophisticated looking menu. It is a semi-formal dining restaurant with wooden tables and chairs and will have a focus on a creating a lively atmosphere. Environment-friendly products will be used, and the menu will be 100% vegetarian. There will be an emphasis on fresh, healthy and delicious food. We will be targeting vegans, vegetarians, health conscious people, people from all age groups, Indians, Australian's as well as other ethnic communities. We need a clean, simple, sophisticated design for the new restaurant menu. Attached is the restaurant logo for reference.

UPDATE:
- We have attached the menu
- We are not looking for any particular type of layout or size (open to suggests). Please suggest this after having a look at the menu contents. However, we will be having one formal menu to be used in the restaurant, and one in brochure form for distribution.
- There are no images at present. If you feel the need of images, please use sample images for now.

Thank you for the entries thus far.
Updates

Target Market(s)

All age groups from different nationalities

Industry/Entity Type

Indian Restaurant

Colors

Designer to choose colors to be used in the design.

Requirements
Nice to have
• This will be printed on environmentally friendly paper.

```html
<!DOCTYPE html>
<html lang="en">
<head>
<meta charset="utf-8">
<title>Spices of Sarani Restaurant – Menu</title>
<link rel="stylesheet" href="https://fonts.googleapis.com/css2?family=Lobster&family=PT+Sans:ital,wght@0,400;0,700;1,400&family=Cinzel:wght@400&display=swap">
<style>
  :root {
    --paper: #f6eed9;
    --grid: rgba(200, 180, 140, 0.14);
    --saffron: #ec9437;
    --leaf: #1d8a45;
    --leaf-dark: #177a3b;
    --ink: #1e1a16;
    --ink-soft: #3a332c;
    --heading: #7a3d12;
    --footer-text: #f3ead4;
  }
  * { margin: 0; padding: 0; box-sizing: border-box; }
  html, body { width: 1200px; height: 852px; overflow: hidden; }
  body {
    position: relative;
    background-color: var(--paper);
    background-image:
      repeating-linear-gradient(0deg, var(--grid) 0 1px, transparent 1px 13px),
      repeating-linear-gradient(90deg, var(--grid) 0 1px, transparent 1px 13px);
    font-family: "PT Sans", Arial, sans-serif;
    color: var(--ink);
  }
  .foliage, .photo, .brand, .section-title, .menu-item, .tagline, .tagline-band { position: absolute; }
  .foliage--top, .foliage--bottom { left: 0; width: 1200px; }
  .foliage--top { top: 0; height: 230px; }
  .foliage--bottom { bottom: 0; height: 140px; }

  .photo { border-radius: 50%; }
  .photo--dosa {
    left: 20px; top: 300px; width: 552px; height: 310px;
    border-radius: 45% 55% 50% 50%;
    background: radial-gradient(ellipse at 55% 50%, rgba(222, 196, 150, 0.55), rgba(236, 220, 190, 0.35) 60%, rgba(246, 238, 217, 0) 75%);
  }
  .photo--soup {
    left: 604px; top: 168px; width: 308px; height: 240px;
    background: radial-gradient(ellipse at 50% 45%, rgba(236, 214, 150, 0.6), rgba(240, 234, 222, 0.55) 55%, rgba(246, 238, 217, 0) 72%);
  }
  .photo--kebab {
    left: 872px; top: 440px; width: 300px; height: 250px;
    background: radial-gradient(ellipse at 50% 50%, rgba(110, 120, 70, 0.38), rgba(170, 170, 120, 0.2) 55%, rgba(246, 238, 217, 0) 72%);
  }

  .brand {
    width: 200px; text-align: center;
    font-family: "PT Sans", Arial, sans-serif; font-weight: 700;
    color: var(--ink); font-size: 19px; line-height: 1.05;
  }
  .brand small { display: block; font-size: 8px; letter-spacing: 2px; margin-top: 2px; }
  .brand--left { left: 350px; top: 76px; }
  .brand--right { left: 586px; top: 54px; }

  .section-title {
    font-family: "Lobster", cursive; font-size: 31px; color: var(--heading);
    letter-spacing: 2px; transform: translateX(-50%); white-space: nowrap;
  }
  .section-title--breakfast { left: 300px; top: 184px; }
  .section-title--soup { left: 874px; top: 186px; }
  .section-title--entree { left: 874px; top: 303px; }

  .menu-item { left: 78px; }
  .menu-item--right { left: 654px; }
  .menu-item__line { display: flex; align-items: baseline; font-size: 13px; font-weight: 700; white-space: nowrap; }
  .menu-item__note { font-size: 6.5px; font-weight: 700; margin-left: 3px; color: var(--ink-soft); }
  .menu-item__dots { flex: 1; overflow: hidden; font-weight: 400; letter-spacing: 0.5px; }
  .menu-item__dots::after { content: "................................................................................................................................................................"; }
  .menu-item__price { font-weight: 700; }
  .menu-item__desc { font-size: 9.8px; font-style: italic; color: var(--ink-soft); margin-top: 5px; white-space: nowrap; }

  .w-dosa { width: 440px; }
  .w-rava { width: 431px; }
  .w-kanda { width: 435px; }
  .w-masala { width: 453px; }
  .w-right { width: 420px; }
  .w-kofta { width: 417px; }

  .tagline-band { left: 588px; top: 812px; width: 596px; height: 40px; background: var(--leaf-dark); opacity: 0.6; }
  .tagline {
    left: 664px; top: 812px; font-family: "Cinzel", serif; font-size: 22px;
    letter-spacing: 4px; color: var(--footer-text); white-space: nowrap;
  }
</style>
</head>
<body>
  <svg class="foliage foliage--top" role="img" aria-label="Orange leafy foliage decoration along the top edge" viewBox="0 0 1200 230" preserveAspectRatio="none">
    <path fill="var(--saffron)" d="M0 0H90L70 40Q50 70 25 65Q10 85 0 80Z"/>
    <path fill="var(--saffron)" d="M175 0H600Q620 40 600 70Q615 110 590 140Q575 175 540 180Q520 215 470 205Q430 225 390 200Q350 210 330 180Q290 185 285 150Q240 140 250 105Q205 95 215 60Q180 45 175 0Z"/>
    <path fill="var(--saffron)" d="M590 0H1200V120Q1180 110 1160 120Q1130 100 1120 70Q1080 60 1050 55Q1000 50 960 58Q920 50 880 55Q830 45 790 55Q770 90 745 110Q720 140 690 130Q660 150 640 125Q610 120 605 90Q585 60 600 35Z"/>
  </svg>

  <div class="photo photo--dosa" role="img" aria-label="Photo of a crispy dosa served with sambar and chutneys"></div>
  <div class="photo photo--soup" role="img" aria-label="Photo of a bowl of creamy soup garnished with mint"></div>
  <div class="photo photo--kebab" role="img" aria-label="Photo of green hara kebab patties with onion rings"></div>

  <div class="brand brand--left">Spices of Sarani<small>Restaurant</small></div>
  <div class="brand brand--right">Spices of Sarani<small>Restaurant</small></div>

  <h2 class="section-title section-title--breakfast">Breakfast</h2>

  <div class="menu-item w-dosa" style="top:238px"><div class="menu-item__line">Dosa/ Vada/ Idli<span class="menu-item__note">served with sambar (Lentil), coconut chutney and tomato chilli chutney</span><span class="menu-item__dots"></span><span class="menu-item__price">$11.9</span></div><p class="menu-item__desc">Crispy crepe made with ground rice and lentils gluten free.</p></div>
  <div class="menu-item w-rava" style="top:277px"><div class="menu-item__line">Rava Dosa<span class="menu-item__dots"></span><span class="menu-item__price">$9.9</span></div><p class="menu-item__desc">Crispy crepe made with ground rice and lentil and onion stuffed with potatoes.</p></div>
  <div class="menu-item w-kanda" style="top:318px"><div class="menu-item__line">Kanda Rava Dosa<span class="menu-item__dots"></span><span class="menu-item__price">$11.9</span></div><p class="menu-item__desc">Crispy crepe made with ground rice and lentil stuffed with potatoes.</p></div>
  <div class="menu-item w-masala" style="top:360px"><div class="menu-item__line">Masala Rava Dosa<span class="menu-item__dots"></span><span class="menu-item__price">$11.9</span></div><p class="menu-item__desc">Crispy crepe made with rice and lentil batter with clarified butter.</p></div>
  <div class="menu-item w-dosa" style="top:397px"><div class="menu-item__line">Dosa/ Vada/ Idli<span class="menu-item__note">served with sambar (Lentil), coconut chutney and tomato chilli chutney</span><span class="menu-item__dots"></span><span class="menu-item__price">$11.9</span></div><p class="menu-item__desc">Crispy crepe made with ground rice and lentils gluten free.</p></div>
  <div class="menu-item w-rava" style="top:436px"><div class="menu-item__line">Rava Dosa<span class="menu-item__dots"></span><span class="menu-item__price">$9.9</span></div><p class="menu-item__desc">Crispy crepe made with ground rice and lentil and onion stuffed with potatoes.</p></div>
  <div class="menu-item w-kanda" style="top:477px"><div class="menu-item__line">Kanda Rava Dosa<span class="menu-item__dots"></span><span class="menu-item__price">$11.9</span></div><p class="menu-item__desc">Crispy crepe made with ground rice and lentil stuffed with potatoes.</p></div>
  <div class="menu-item w-masala" style="top:519px"><div class="menu-item__line">Masala Rava Dosa<span class="menu-item__dots"></span><span class="menu-item__price">$11.9</span></div><p class="menu-item__desc">Crispy crepe made with rice and lentil batter with clarified butter.</p></div>
  <div class="menu-item w-dosa" style="top:557px"><div class="menu-item__line">Dosa/ Vada/ Idli<span class="menu-item__note">served with sambar (Lentil), coconut chutney and tomato chilli chutney</span><span class="menu-item__dots"></span><span class="menu-item__price">$11.9</span></div><p class="menu-item__desc">Crispy crepe made with ground rice and lentils gluten free.</p></div>
  <div class="menu-item w-rava" style="top:596px"><div class="menu-item__line">Rava Dosa<span class="menu-item__dots"></span><span class="menu-item__price">$9.9</span></div><p class="menu-item__desc">Crispy crepe made with ground rice and lentil and onion stuffed with potatoes.</p></div>
  <div class="menu-item w-kanda" style="top:637px"><div class="menu-item__line">Kanda Rava Dosa<span class="menu-item__dots"></span><span class="menu-item__price">$11.9</span></div><p class="menu-item__desc">Crispy crepe made with ground rice and lentil stuffed with potatoes.</p></div>
  <div class="menu-item w-masala" style="top:679px"><div class="menu-item__line">Masala Rava Dosa<span class="menu-item__dots"></span><span class="menu-item__price">$11.9</span></div><p class="menu-item__desc">Crispy crepe made with rice and lentil batter with clarified butter.</p></div>

  <h2 class="section-title section-title--soup">Soup of the Day</h2>
  <div class="menu-item menu-item--right w-right" style="top:238px"><div class="menu-item__line">Cream of tomato with crotons<span class="menu-item__dots"></span><span class="menu-item__price">$4.9</span></div></div>
  <div class="menu-item menu-item--right w-right" style="top:261px"><div class="menu-item__line">Curried pumpkin with shallots<span class="menu-item__dots"></span><span class="menu-item__price">$4.9</span></div></div>

  <h2 class="section-title section-title--entree">Entree (Tapas)</h2>
  <div class="menu-item menu-item--right w-kofta" style="top:357px"><div class="menu-item__line">Kamal Kofta (4pcs)<span class="menu-item__dots"></span><span class="menu-item__price">$6.9</span></div><p class="menu-item__desc">Crispy potatoes and paneer with cashews, coriander fresh chilli spice croquets.</p></div>
  <div class="menu-item menu-item--right w-right" style="top:402px"><div class="menu-item__line">Hara Kebab (4pcs)<span class="menu-item__dots"></span><span class="menu-item__price">$6.9</span></div><p class="menu-item__desc">Fresh baby spinach ricotta cheese mash potatoes ginger fresh coriander fresh chilli patty.</p></div>
  <div class="menu-item menu-item--right w-kofta" style="top:450px"><div class="menu-item__line">Kamal Kofta (4pcs)<span class="menu-item__dots"></span><span class="menu-item__price">$6.9</span></div><p class="menu-item__desc">Crispy crepe made with ground rice and lentils gluten free.</p></div>
  <div class="menu-item menu-item--right w-right" style="top:496px"><div class="menu-item__line">Hara Kebab (4pcs)<span class="menu-item__dots"></span><span class="menu-item__price">$6.9</span></div><p class="menu-item__desc">Fresh baby spinach ricotta cheese mash potatoes ginger fresh coriander fresh chilli patty.</p></div>
  <div class="menu-item menu-item--right w-kofta" style="top:539px"><div class="menu-item__line">Kamal Kofta (4pcs)<span class="menu-item__dots"></span><span class="menu-item__price">$6.9</span></div><p class="menu-item__desc">Crispy crepe made with ground rice and lentils gluten free.</p></div>
  <div class="menu-item menu-item--right w-right" style="top:585px"><div class="menu-item__line">Hara Kebab (4pcs)<span class="menu-item__dots"></span><span class="menu-item__price">$6.9</span></div><p class="menu-item__desc">Fresh baby spinach ricotta cheese mash potatoes ginger fresh coriander fresh chilli patty.</p></div>
  <div class="menu-item menu-item--right w-kofta" style="top:628px"><div class="menu-item__line">Kamal Kofta (4pcs)<span class="menu-item__dots"></span><span class="menu-item__price">$6.9</span></div><p class="menu-item__desc">Crispy crepe made with ground rice and lentils gluten free.</p></div>
  <div class="menu-item menu-item--right w-right" style="top:673px"><div class="menu-item__line">Hara Kebab (4pcs)<span class="menu-item__dots"></span><span class="menu-item__price">$6.9</span></div><p class="menu-item__desc">Fresh baby spinach ricotta cheese mash potatoes ginger fresh coriander fresh chilli patty.</p></div>

  <svg class="foliage foliage--bottom" role="img" aria-label="Green leafy foliage decoration along the bottom edge" viewBox="0 0 1200 140" preserveAspectRatio="none">
    <path fill="var(--leaf)" d="M0 75Q40 60 70 70Q110 40 160 50Q200 35 240 55Q280 60 300 85Q340 80 380 95Q420 100 470 80Q500 55 540 45Q580 40 600 60Q620 75 640 90Q700 100 760 95Q820 95 880 100Q910 70 950 65Q990 30 1040 25Q1080 20 1120 35Q1160 30 1200 45V140H0Z"/>
  </svg>
  <div class="tagline-band"></div>
  <p class="tagline">The Essence of Indian Cuisine</p>
</body>
</html>
```